Succession & Estate Planning firm needs a double-sided one page client handout

We need a client hand-out that highlights the top 10 Reasons to get a Pension Plan. It will need the 10 reasons as headings, with a short description of each reason (attached Word doc). It should communicate that a Pension Plan is flexible and provides security. Our usual client is a business owner/medical professional/entrepreneur. Have a look at our website for more info about our business www.marvelko.ca Our logo colours are 83c242, 3b3839, d5d5d5 We like clean, modern, info-graphics, not too cluttered, not too loudWe would like the ability to update the text/content ourselves, in the future.

```html
<!DOCTYPE html>
<html lang="en">
<head>
<meta charset="utf-8">
<title>Marvelko – Top 10 Reasons Why an FPP Serves Your Family Enterprise</title>
<link href="https://fonts.googleapis.com/css2?family=Bebas+Neue&family=Roboto:wght@400;700&family=Roboto+Condensed:wght@400;700&display=swap" rel="stylesheet">
<style>
  :root {
    --green: #83c242;
    --charcoal: #3b3839;
    --silver: #d5d5d5;
    --ink: #2a2829;
    --paper: #ffffff;
    --backdrop: #9a9a9a;
  }
  * { box-sizing: border-box; margin: 0; padding: 0; }
  html, body { width: 1200px; height: 800px; overflow: hidden; }
  body { background: var(--backdrop); position: relative; font-family: "Roboto Condensed", sans-serif; color: var(--ink); }

  .page { position: absolute; top: 68px; width: 470px; height: 664px; background: var(--paper); overflow: hidden; }
  .page--cover { left: 103px; }
  .page--reasons { left: 629px; }

  /* Cover */
  .cover-header { position: absolute; left: 0; top: 0; width: 100%; height: 126px; background: var(--charcoal); display: flex; align-items: center; justify-content: center; }
  .brand-name { font-family: "Roboto", sans-serif; font-weight: 400; font-size: 30px; letter-spacing: 5px; color: var(--paper); }
  .cover-photo { position: absolute; left: 0; top: 126px; width: 100%; height: 308px;
    background: radial-gradient(ellipse at 75% 35%, #f3e3b0 0%, rgba(243,227,176,0) 45%),
                linear-gradient(180deg, #8fa35a 0%, #b8b26e 45%, #a58a5e 72%, #c9b69a 100%); }
  .cover-title { position: absolute; left: 0; top: 0; width: 100%; height: 100%; pointer-events: none;
    font-family: "Bebas Neue", sans-serif; font-weight: 400; line-height: 1; color: var(--charcoal); }
  .title-line { position: absolute; left: 27px; white-space: nowrap; transform: scaleX(0.75); transform-origin: left top; }
  .title-line--top { top: 450px; font-size: 66px; }
  .title-line--middle { top: 510px; font-size: 54px; }
  .title-line--bottom { top: 560px; font-size: 40px; }
  .accent { color: var(--green); }
  .cover-sprout { position: absolute; left: 321px; top: 468px; width: 100px; height: 116px;
    background: radial-gradient(ellipse at 45% 40%, #8fcf4a 0%, #a9d978 45%, rgba(255,255,255,0) 72%); }
  .cover-footer { position: absolute; left: 0; bottom: 0; width: 100%; height: 44px; background: var(--charcoal); display: flex; align-items: center; justify-content: center; }
  .cover-footer a { font-family: "Roboto", sans-serif; font-weight: 700; font-size: 14px; color: var(--paper); text-decoration: none; }

  /* Reasons page */
  .reasons-photo { position: absolute; left: 0; top: 0; width: 100%; height: 158px;
    background: radial-gradient(ellipse at 55% 40%, #8fbf3a 0%, rgba(143,191,58,0) 55%),
                linear-gradient(90deg, #1f2a18 0%, #4e6a2a 35%, #3d4a26 65%, #8a5a36 100%); }
  .reasons-band { position: absolute; left: 0; top: 158px; width: 100%; height: 30px; background: var(--green); display: flex; align-items: center; justify-content: center; }
  .reasons-band h1 { font-family: "Bebas Neue", sans-serif; font-weight: 400; font-size: 21px; color: var(--paper); letter-spacing: 0; }

  .timeline { position: absolute; top: 210px; width: 3px; height: 380px; background: var(--ink); }
  .timeline--left { left: 39px; }
  .timeline--right { left: 266px; }

  .reason { position: absolute; width: 210px; }
  .reason--left { left: 26px; }
  .reason--right { left: 252px; }
  .reason-number { position: absolute; left: 0; top: -4px; width: 29px; height: 30px; background: var(--green); display: flex; align-items: center; justify-content: center;
    font-family: "Roboto Condensed", sans-serif; font-weight: 700; font-size: 27px; color: var(--ink); line-height: 1; }
  .reason--ten .reason-number { width: 31px; font-size: 23px; letter-spacing: -1px; }
  .reason-body { margin-left: 38px; width: 154px; }
  .reason-body h2 { font-family: "Roboto", sans-serif; font-weight: 700; font-size: 9px; line-height: 11px; color: var(--ink); margin-bottom: 2px; }
  .reason-body p { font-size: 6.8px; line-height: 9.4px; text-align: justify; color: #333; }

  .reasons-footer { position: absolute; left: 0; bottom: 0; width: 100%; height: 52px; background: var(--charcoal); color: var(--paper);
    display: flex; align-items: center; justify-content: space-between; padding: 0 24px 0 25px; }
  .contact { display: flex; align-items: center; gap: 6px; font-size: 12px; }
  .contact svg { width: 17px; height: 17px; flex: none; }
  .contact--address { font-size: 10px; line-height: 12px; }
</style>
</head>
<body>

<section class="page page--cover">
  <header class="cover-header">
    <span class="brand-name">MARVELKO</span>
  </header>
  <div class="cover-photo" role="img" aria-label="Photo of a small green seedling growing from a glass jar filled with coins on a wooden table"></div>
  <h1 class="cover-title">
    <span class="title-line title-line--top">Top <span class="accent">10</span> Reasons</span>
    <span class="title-line title-line--middle">Why an <span class="accent">FPP Serves</span></span>
    <span class="title-line title-line--bottom">Your <span class="accent">Family</span> Enterprise</span>
  </h1>
  <div class="cover-sprout" role="img" aria-label="Green sprout illustration"></div>
  <footer class="cover-footer"><a href="#">www.marvelko.ca</a></footer>
</section>

<section class="page page--reasons">
  <div class="reasons-photo" role="img" aria-label="Photo of young green sprouts growing against a soft blurred background"></div>
  <div class="reasons-band"><h1>Top 10 Reasons Why an FPP Serves Your Family Enterprise</h1></div>

  <div class="timeline timeline--left"></div>
  <div class="timeline timeline--right"></div>

  <article class="reason reason--left" style="top:223px">
    <div class="reason-number">1</div>
    <div class="reason-body">
      <h2>CREATE SIGNIFICANT DEDUCTIONS</h2>
      <p>The FPP creates significant tax deductions, which can be used to keep the business under the small business rate or applied to the high rate, a bigger bang for the buck</p>
    </div>
  </article>
  <article class="reason reason--left" style="top:299px">
    <div class="reason-number">2</div>
    <div class="reason-body">
      <h2>DELIBERATE, PLANNED, FUTURE INCOME</h2>
      <p>An income for beyond the last day at the office</p>
    </div>
  </article>
  <article class="reason reason--left" style="top:374px">
    <div class="reason-number">3</div>
    <div class="reason-body">
      <h2>PAST BUY BACK</h2>
      <p>Most owners invest, first, in the business. The FPP offers the ability to go back and recover lost years when they did not buy RRSPs...and pass the tax savings onto their company</p>
    </div>
  </article>
  <article class="reason reason--left" style="top:450px">
    <div class="reason-number">4</div>
    <div class="reason-body">
      <h2>CREDITOR PROOF</h2>
      <p>All Assets held in an FPP are creditor proof, including RRSPs, and planned pension contributions receive “super-priority” status, which rank above the claims of secured creditors, like major commercial lenders and banks</p>
    </div>
  </article>
  <article class="reason reason--left" style="top:528px">
    <div class="reason-number">5</div>
    <div class="reason-body">
      <h2>FLEXIBILITY</h2>
      <p>Owners know that cash flows can swing wildly with the business cycle. An FPP offers the flexibility to flip between DB and DC accounts in order to conserve cash, smooth income during volatile years, and recover assets when things improve.</p>
    </div>
  </article>

  <article class="reason reason--right" style="top:223px">
    <div class="reason-number">6</div>
    <div class="reason-body">
      <h2>PRESERVE THE LIFETIME CAPITAL GAINS EXEMPTION</h2>
      <p>a. Create $1.6 Million++ of Tax Free Capital Gains. The significant deductions created in an FPP can be used to purify a corporation with passive assets, which can help preserve the shareholders’ lifetime capital gains exemption</p>
    </div>
  </article>
  <article class="reason reason--right" style="top:304px">
    <div class="reason-number">7</div>
    <div class="reason-body">
      <h2>INTERGENERATIONAL WEALTH TRANSFER</h2>
      <p>Unlike RRSPs that eventually trigger a taxable disposition upon death, an FPP has the ability to pass, tax deferred, to the next generation of family business owners.</p>
    </div>
  </article>
  <article class="reason reason--right" style="top:381px">
    <div class="reason-number">8</div>
    <div class="reason-body">
      <h2>ALL PAGES</h2>
      <p>An FPP can benefit all entrepreneurs between ages 18-71</p>
    </div>
  </article>
  <article class="reason reason--right" style="top:433px">
    <div class="reason-number">9</div>
    <div class="reason-body">
      <h2>CONSERVE THE SMALL BUSINESS DEDUCTION</h2>
      <p>Investment income inside an FPP grows tax exempt and does not create passive income as outlined under the 2018 “Passive Income Measures”. Therefore, business owners that redirect corporate resources to fund their pension assets will not jeopardize their low corporate tax rate on profits and in associated companies</p>
    </div>
  </article>
  <article class="reason reason--right reason--ten" style="top:539px">
    <div class="reason-number">10</div>
    <div class="reason-body">
      <h2>BROADER INVESTMENT OPTIONS</h2>
      <p>An FPP allows entrepreneurs to invest in what they like: real estate, other businesses and/or franchises, private equity, public equity, exempt markets, etc. The possibilities are up to the imagination of the entrepreneur and their advisors.</p>
    </div>
  </article>

  <footer class="reasons-footer">
    <div class="contact">
      <svg viewBox="0 0 20 20" aria-hidden="true"><circle cx="10" cy="10" r="9" fill="none" stroke="#fff" stroke-width="1.5"/><path d="M7 5.5l1.6 2.4-1 1.2c.7 1.4 1.8 2.5 3.2 3.2l1.2-1 2.4 1.6-.8 1.6c-3.6-.3-6.9-3.6-7.2-7.2z" fill="#fff"/></svg>
      <span>1-877-555-0142</span>
    </div>
    <div class="contact">
      <svg viewBox="0 0 20 20" aria-hidden="true"><circle cx="10" cy="10" r="9" fill="none" stroke="#fff" stroke-width="1.5"/><circle cx="10" cy="10" r="5.5" fill="none" stroke="#fff" stroke-width="1.2"/><ellipse cx="10" cy="10" rx="2.3" ry="5.5" fill="none" stroke="#fff" stroke-width="1"/><line x1="4.5" y1="10" x2="15.5" y2="10" stroke="#fff" stroke-width="1"/></svg>
      <span>www.marvelko.ca</span>
    </div>
    <div class="contact contact--address">
      <svg viewBox="0 0 20 20" aria-hidden="true"><circle cx="10" cy="10" r="9" fill="none" stroke="#fff" stroke-width="1.5"/><path d="M10 4.5l5.5 5h-1.6v5h-2.6v-3.2H8.7v3.2H6.1v-5H4.5z" fill="#fff"/></svg>
      <span>118 – 402 Harbour Road Regina,<br>Saskatchewan S4P 2K9</span>
    </div>
  </footer>
</section>

</body>
</html>
```